Design a WordPress layout for a home loans company

The home loans company in question is going through a rebrand and needs a new website layout.
Sites they like: http://www.brightnestlending.com.au/
Current logo: Attached.
Colours to be used: As per those used in logo.
Primary: #71aa3d
Secondary: #130e10
Pages to be designed:
- Homepage
- Internal services page
Menu items for display purposes:
- Home
- About Us
- Speak to a Broker
- Articles
- Contact Us
A modern design with simplicity is key.
For copy, dummy text such as Lorem ipsum will be fine.
If you would like anything elso, please ask.
Target Market(s)
25-40 year old
Mostly female
Buying their first home in most cases
Industry/Entity Type
Mortgage Brokerage
Number of Pages Required
2 page
Colors
Designer to choose colors to be used in the design.
Look and feel

```html
<!DOCTYPE html>
<html lang="en">
<head>
<meta charset="utf-8">
<title>Maple Home Loans — Homepage</title>
<link href="https://fonts.googleapis.com/css2?family=Lato:wght@400;700;900&display=swap" rel="stylesheet">
<style>
:root{
  --green:#71aa3d;
  --green-dark:#5e9130;
  --ink:#130e10;
  --text:#555;
  --muted:#888;
  --light:#f1f1f1;
  --nav:#2a2a2a;
  --footer:#2b2b2b;
  --footer-deep:#1e1e1e;
  --white:#fff;
}
*{box-sizing:border-box;margin:0;padding:0}
html,body{width:1200px;height:3440px;overflow:hidden}
body{font-family:'Lato',sans-serif;color:var(--text);background:var(--white);position:relative}
.abs{position:absolute}
h2.section-title{font-weight:900;font-size:38px;color:var(--green);text-align:center;letter-spacing:.5px}
p{font-size:15px;line-height:1.65}

/* header */
.site-header{top:0;left:0;width:1200px;height:120px}
.brand{left:74px;top:22px;display:flex;align-items:center;gap:12px}
.brand-mark{width:18px;height:18px;background:var(--green)}
.brand-name{font-weight:900;font-size:30px;color:var(--green);line-height:1}
.top-contacts{right:60px;top:26px;display:flex;gap:40px}
.top-contact{display:flex;gap:12px;align-items:flex-start;font-size:13px;line-height:1.5;color:var(--text);width:200px}
.top-contact.phone{width:150px}
.ico-circle{width:34px;height:34px;border-radius:50%;border:2px solid var(--green);flex:none;display:flex;align-items:center;justify-content:center}

.main-nav{top:120px;left:0;width:1200px;height:48px;background:var(--nav)}
.main-nav ul{list-style:none;display:flex;position:absolute;left:70px;top:0;height:48px}
.main-nav li{color:#ddd;font-size:14px;font-weight:700;padding:0 24px;line-height:48px;text-transform:uppercase}
.main-nav li.active{background:var(--green);color:var(--white)}
.enquire{right:70px;top:0;height:48px;line-height:48px;padding:0 26px;background:var(--green);color:var(--white);font-weight:900;font-size:17px}

/* hero */
.hero{top:168px;left:0;width:1200px;height:530px;background:linear-gradient(90deg,#6f6a66,#a8a39e 45%,#8a8580);}
.hero-shade{inset:0;background:rgba(30,30,30,.35)}
.hero-content{left:0;top:170px;width:1200px;text-align:center;color:var(--white)}
.hero-content h1{font-weight:900;font-size:64px;letter-spacing:1px}
.hero-rule{width:160px;height:3px;background:var(--white);margin:10px auto 16px}
.hero-content p{width:600px;margin:0 auto;font-size:15px}

/* welcome */
.welcome{top:720px;left:0;width:1200px;height:290px;text-align:center}
.welcome p{width:920px;margin:0 auto;font-size:14px}
.rule-green{width:80px;height:3px;background:var(--green);margin:14px auto 28px}

/* features */
.features{top:1010px;left:0;width:1200px;height:545px;background:var(--light)}
.photo{border:none}
.family{left:0;top:0;width:600px;height:545px;background:linear-gradient(160deg,#c7b7a3,#e8e3dc 55%,#a7b3c4)}
.feature-list{left:640px;top:55px;width:480px}
.feature{display:flex;gap:30px;margin-bottom:46px}
.feature-icon{width:82px;height:82px;border-radius:50%;background:var(--green);flex:none;display:flex;align-items:center;justify-content:center}
.feature h3{color:var(--green);font-weight:700;font-size:26px;margin-bottom:6px}
.feature p{font-size:13px;line-height:1.6}

/* about */
.about{top:1600px;left:0;width:1200px;height:420px}
.about-text{left:80px;top:40px;width:440px}
.about-text h2{font-weight:900;font-size:38px;color:var(--green)}
.about-text .rule-green{margin:12px 0 22px}
.about-text p{font-size:14px;margin-bottom:18px}
.btn{display:inline-block;background:var(--green);color:var(--white);font-weight:900;font-size:16px;padding:12px 22px;text-transform:uppercase;margin-right:10px}
.about-frame{left:640px;top:40px;width:460px;height:300px;border:10px solid var(--green)}
.about-photo{left:620px;top:60px;width:460px;height:300px;background:linear-gradient(120deg,#9fb18a,#d9d2c3 50%,#8e8d86)}

/* broker */
.broker{top:2050px;left:0;width:1200px;height:290px;background:var(--light);text-align:center;padding-top:40px}
.broker h2{color:var(--ink)}
.broker p{width:580px;margin:0 auto;font-size:14px}
.broker .rule-green{margin:14px auto 18px}
.search{display:flex;justify-content:center;margin-top:26px}
.search-input{width:430px;height:44px;background:var(--white);border:1px solid #ddd;font-size:13px;color:var(--muted);text-align:left;padding:0 16px;line-height:44px}
.search-btn{height:44px;line-height:44px;padding:0 22px;background:var(--green);color:var(--white);font-weight:900;font-size:16px}

/* articles */
.articles{top:2380px;left:0;width:1200px;height:540px;text-align:center}
.articles .rule-green{margin:12px auto 30px}
.article-card{left:80px;top:100px;width:1040px;height:380px;background:var(--light);display:flex;text-align:left}
.article-photo{width:520px;height:380px;background:linear-gradient(135deg,#c9ccd0,#eee9e2 50%,#a9a4a0);flex:none}
.article-body{padding:30px 36px}
.article-body h3{font-size:24px;color:var(--ink);font-weight:700;margin-bottom:16px}
.meta{display:flex;gap:30px;font-size:13px;color:var(--muted);margin-bottom:18px;align-items:center}
.meta span{display:flex;gap:8px;align-items:center}
.article-body p{font-size:14px;margin-bottom:14px}
.arrow{top:260px;width:30px;height:40px}

/* footer */
.site-footer{top:3010px;left:0;width:1200px;height:430px;background:var(--footer)}
.contact-strip{top:2950px;left:80px;width:1040px;height:140px;background:var(--green);display:flex;color:var(--white);align-items:center;padding:0 60px;gap:50px}
.contact-item{display:flex;gap:18px;align-items:center;width:300px}
.contact-item .ico-circle{border-color:var(--white);width:50px;height:50px}
.contact-item strong{display:block;font-size:22px;font-weight:700}
.contact-item span{font-size:14px;line-height:1.5}
.footer-links{top:3135px;left:80px;display:flex;gap:36px;color:#ccc;font-size:14px}
.social{top:3120px;right:80px;display:flex;gap:10px}
.social i{width:40px;height:40px;border-radius:50%;background:var(--white);display:block}
.footer-rule{top:3185px;left:80px;width:1040px;height:1px;background:#444}
.newsletter{top:3215px;left:80px;color:#ccc;font-size:14px}
.news-form{display:flex;margin-top:22px}
.news-input{width:340px;height:44px;border:1px solid #555;color:#888;font-size:13px;padding:0 14px;line-height:44px}
.news-btn{width:70px;height:44px;background:var(--green);display:flex;align-items:center;justify-content:center}
.footer-brand{top:3240px;right:80px;display:flex;align-items:center;gap:12px}
.copyright{top:3370px;left:0;width:1200px;height:70px;background:var(--footer-deep);color:#aaa;font-size:13px;text-align:center;line-height:70px}
</style>
</head>
<body>

<header class="site-header abs">
  <div class="brand abs"><span class="brand-mark"></span><span class="brand-name">Maple Home Loans</span></div>
  <div class="top-contacts abs">
    <div class="top-contact">
      <span class="ico-circle"><svg width="14" height="18" viewBox="0 0 14 18"><path d="M7 0a7 7 0 0 0-7 7c0 5 7 11 7 11s7-6 7-11a7 7 0 0 0-7-7zm0 10a3 3 0 1 1 0-6 3 3 0 0 1 0 6z" fill="#71aa3d"/></svg></span>
      <span>Lorem ipsum is simply dummy text of the printing</span>
    </div>
    <div class="top-contact phone">
      <span class="ico-circle"><svg width="16" height="16" viewBox="0 0 24 24"><path d="M6.6 10.8a15 15 0 0 0 6.6 6.6l2.2-2.2a1 1 0 0 1 1-.25 11.4 11.4 0 0 0 3.6.57 1 1 0 0 1 1 1V20a1 1 0 0 1-1 1A17 17 0 0 1 3 4a1 1 0 0 1 1-1h3.5a1 1 0 0 1 1 1c0 1.25.2 2.45.57 3.57a1 1 0 0 1-.25 1z" fill="#71aa3d"/></svg></span>
      <span>Call Us Now<br>1300 555 018</span>
    </div>
  </div>
</header>

<nav class="main-nav abs">
  <ul>
    <li class="active">Home</li><li>About</li><li>Speak to Broker</li><li>Articles</li><li>Contact</li>
  </ul>
  <div class="enquire abs">ENQUIRE</div>
</nav>

<section class="hero abs">
  <div class="abs photo" role="img" aria-label="Broker meeting a young couple at a desk" style="inset:0"></div>
  <div class="hero-shade abs"></div>
  <div class="hero-content abs">
    <h1>MAPLE HOME<br>LOANS</h1>
    <div class="hero-rule"></div>
    <p>Lorem Ipsum is simply dummy text of the printing and typesetting industry. Lorem Ipsum has been the industry's standard dummy text ever since the 1500s.</p>
  </div>
</section>

<section class="welcome abs">
  <h2 class="section-title">WELCOME TO MAPLE HOME LOANS</h2>
  <div class="rule-green"></div>
  <p>Lorem Ipsum is simply dummy text of the printing and typesetting industry. Lorem Ipsum has been the industry's standard dummy text ever since the 1500s, when an unknown printer took a galley of type and scrambled it to make a type specimen book. It has survived not only five centuries, but also the leap into electronic typesetting.</p>
  <p style="margin-top:16px">It has survived not only five centuries, but also the leap into electronic typesetting, remaining essentially unchanged. It was popularised in the 1960s with the release of Letraset sheets containing Lorem Ipsum passages.</p>
</section>

<section class="features abs">
  <div class="family abs photo" role="img" aria-label="Smiling young family of four embracing"></div>
  <div class="feature-list abs">
    <div class="feature">
      <span class="feature-icon"><svg width="38" height="38" viewBox="0 0 24 24"><path d="M12 2a7 7 0 0 0-7 7c0 5 7 13 7 13s7-8 7-13a7 7 0 0 0-7-7zm0 10a3 3 0 1 1 0-6 3 3 0 0 1 0 6z" fill="#fff"/></svg></span>
      <div><h3>Local experts</h3><p>With brokers all across Australia, you can be confident there is a professional near you with in-depth knowledge of your local area.</p></div>
    </div>
    <div class="feature">
      <span class="feature-icon"><svg width="40" height="40" viewBox="0 0 24 24"><path d="M5 12l5 5 9-10" stroke="#fff" stroke-width="3" fill="none" stroke-linecap="round" stroke-linejoin="round"/></svg></span>
      <div><h3>Ongoing trusted advice</h3><p>We believe in the power of advice to help you both now and into the future as your circumstances and needs change.</p></div>
    </div>
    <div class="feature">
      <span class="feature-icon"><svg width="38" height="38" viewBox="0 0 24 24"><path d="M2 10h4v11H2zM8 21h9.5a2 2 0 0 0 2-1.6l1.4-7A2 2 0 0 0 19 10h-5l.8-4.2A2 2 0 0 0 12.8 3L8 9z" fill="#fff"/></svg></span>
      <div><h3>Greater choice</h3><p>Financial solutions aren't one-size-fits-all. Ask our extensive range of lenders and products to find the right solution.</p></div>
    </div>
  </div>
</section>

<section class="about abs">
  <div class="about-text abs">
    <h2>ABOUT MAPLE HOME LOANS</h2>
    <div class="rule-green"></div>
    <p>Lorem Ipsum is simply dummy text of the printing and typesetting industry. Lorem Ipsum has been the industry's standard dummy text ever since the 1500s, when an unknown printer took a galley of type and scrambled it to make a type specimen book.</p>
    <p>Lorem Ipsum is simply dummy text of the printing and typesetting industry. Lorem Ipsum has been the industry's standard dummy text.</p>
    <span class="btn">Know more</span><span class="btn">Contact us</span>
  </div>
  <div class="about-frame abs"></div>
  <div class="about-photo abs photo" role="img" aria-label="Couple standing in front of their new house"></div>
</section>

<section class="broker abs">
  <h2 class="section-title" style="color:var(--ink)">FIND A LOCAL BROKER</h2>
  <div class="rule-green"></div>
  <p>Lorem Ipsum is simply dummy text of the printing and typesetting industry. Lorem Ipsum has been the industry's standard dummy text ever since the 1500s.</p>
  <div class="search"><div class="search-input">Suburb town or postcode</div><div class="search-btn">FIND BROKER</div></div>
</section>

<section class="articles abs">
  <h2 class="section-title">LATEST ARTICLES</h2>
  <div class="rule-green"></div>
  <svg class="arrow abs" style="left:20px" viewBox="0 0 30 40"><path d="M20 8L8 20l12 12" stroke="#444" stroke-width="3" fill="none"/></svg>
  <svg class="arrow abs" style="right:20px" viewBox="0 0 30 40"><path d="M10 8l12 12-12 12" stroke="#444" stroke-width="3" fill="none"/></svg>
  <article class="article-card abs">
    <div class="article-photo photo" role="img" aria-label="Young couple reviewing loan papers with a broker"></div>
    <div class="article-body">
      <h3>Lorem Ipsum is simply dummy text of the printing.</h3>
      <div class="meta">
        <span><svg width="14" height="14" viewBox="0 0 14 14"><rect x="1" y="2" width="12" height="11" fill="none" stroke="#71aa3d" stroke-width="1.5"/><path d="M1 5h12" stroke="#71aa3d" stroke-width="1.5"/></svg>Aug 12, 2016</span>
        <span><svg width="14" height="14" viewBox="0 0 14 14"><circle cx="7" cy="4" r="3" fill="#71aa3d"/><path d="M1 14a6 6 0 0 1 12 0z" fill="#71aa3d"/></svg>By, Name Surname</span>
      </div>
      <p>Lorem Ipsum is simply dummy text of the printing and typesetting industry. Lorem Ipsum has been the industry's standard dummy text ever since the 1500s, when an unknown printer took a galley of type and scrambled it to make a type specimen book.</p>
      <p>It has survived not only five centuries, but also the leap into electronic typesetting.</p>
    </div>
  </article>
</section>

<footer class="site-footer abs"></footer>
<div class="contact-strip abs">
  <div class="contact-item">
    <span class="ico-circle"><svg width="18" height="22" viewBox="0 0 14 18"><path d="M7 0a7 7 0 0 0-7 7c0 5 7 11 7 11s7-6 7-11a7 7 0 0 0-7-7zm0 10a3 3 0 1 1 0-6 3 3 0 0 1 0 6z" fill="#fff"/></svg></span>
    <span>Lorem Ipsum is simply<br>dummy text of the printing</span>
  </div>
  <div class="contact-item">
    <span class="ico-circle"><svg width="20" height="20" viewBox="0 0 24 24"><path d="M6.6 10.8a15 15 0 0 0 6.6 6.6l2.2-2.2a1 1 0 0 1 1-.25 11.4 11.4 0 0 0 3.6.57 1 1 0 0 1 1 1V20a1 1 0 0 1-1 1A17 17 0 0 1 3 4a1 1 0 0 1 1-1h3.5a1 1 0 0 1 1 1c0 1.25.2 2.45.57 3.57a1 1 0 0 1-.25 1z" fill="#fff"/></svg></span>
    <span><strong>Phone</strong>1300 555 018</span>
  </div>
  <div class="contact-item">
    <span class="ico-circle"><svg width="22" height="16" viewBox="0 0 22 16"><rect x="1" y="1" width="20" height="14" fill="none" stroke="#fff" stroke-width="2"/><path d="M1 1l10 8 10-8" stroke="#fff" stroke-width="2" fill="none"/></svg></span>
    <span><strong>Email</strong>hello@maplehomeloans.com.au</span>
  </div>
</div>
<div class="footer-links abs"><span>Home</span><span>About</span><span>Speak to broker</span><span>Article</span><span>Contact</span></div>
<div class="social abs"><i></i><i></i><i></i></div>
<div class="footer-rule abs"></div>
<div class="newsletter abs">
  Get valuable content every day. Subscribe to our newsletter.
  <div class="news-form"><div class="news-input">Enter Your Email</div><div class="news-btn"><svg width="22" height="16" viewBox="0 0 22 16"><rect x="1" y="1" width="20" height="14" fill="none" stroke="#fff" stroke-width="2"/><path d="M1 1l10 8 10-8" stroke="#fff" stroke-width="2" fill="none"/></svg></div></div>
</div>
<div class="footer-brand abs"><span class="brand-mark"></span><span class="brand-name">Maple Home Loans</span></div>
<div class="copyright abs">MAPLE HOME LOANS, 2016 · All Rights Reserved.</div>

</body>
</html>
```